New counselling and hypnotherapy business

I'd like a flyer which is relevant to people who want support and to improve their wellbeing which follows the same theme as my website: http://wrenlowtherapy.sitepailo.com
And emphasise that whatever the area of concern, development or growth and I can tailor my knowledge and skills to help.

I'd like to use the same logo and my emphasis is to draw the audience in...therapy and counselling is for people who are "stuck" and having a difficult time...it can also be useful has a personal development tool.

Hypnotherapy

```html
<!DOCTYPE html>
<html lang="en">
<head>
<meta charset="utf-8">
<title>Wrenlow Counselling &amp; Hypnotherapy – Flyer</title>
<link href="https://fonts.googleapis.com/css2?family=Arimo:wght@400;700&display=swap" rel="stylesheet">
<style>
  :root {
    --purple: #8b4c88;
    --purple-dark: #6e3a6c;
    --green: #1f8a46;
    --green-dark: #136a33;
    --paper: #ffffff;
    --mist: #e9e9ea;
    --ink-light: #ffffff;
  }
  * { box-sizing: border-box; margin: 0; padding: 0; }
  html, body { width: 857px; height: 1200px; overflow: hidden; background: var(--paper); }
  .flyer {
    position: relative; width: 857px; height: 1200px; overflow: hidden;
    font-family: "Arimo", Arial, sans-serif;
    background: linear-gradient(to bottom, var(--paper) 0, var(--paper) 320px, var(--mist) 560px, #f4f4f5 1200px);
  }
  .brand { position: absolute; left: 48px; top: 34px; display: flex; align-items: center; gap: 18px; }
  .brand-mark { width: 70px; height: 70px; border-radius: 50%; background: var(--purple); }
  .brand-name { color: var(--purple); font-size: 27px; font-weight: 400; line-height: 1.2; }
  .quote {
    position: absolute; left: 362px; top: 46px; width: 470px;
    color: var(--purple); font-size: 22.5px; line-height: 1.32;
  }
  .nav {
    position: absolute; left: 0; top: 250px; width: 857px; height: 64px;
    background: linear-gradient(to bottom, #2aa158, var(--green) 55%, var(--green-dark));
    display: flex; align-items: center; padding-left: 38px;
  }
  .nav span { color: var(--ink-light); font-size: 25px; padding: 0 22px; border-right: 2px solid var(--ink-light); }
  .nav span:first-child { padding-left: 0; }
  .nav span:last-child { border-right: none; }
  .section-title {
    position: absolute; left: 34px; width: 795px;
    color: var(--green-dark); font-size: 25px; padding-bottom: 6px;
    border-bottom: 3px solid var(--green);
  }
  .panel { position: absolute; left: 34px; width: 795px; background: var(--purple); color: var(--ink-light); }
  .panel h3 { font-size: 18px; font-weight: 700; margin-bottom: 4px; }
  .panel p { font-size: 16.5px; line-height: 1.3; }
  .photo { border: 3px solid var(--ink-light); }
  .panel-counselling { top: 382px; height: 150px; }
  .panel-counselling .photo { position: absolute; left: 42px; top: 12px; width: 166px; height: 123px;
    background: linear-gradient(135deg, #d9c7a3, #a88a63 55%, #6d5640); }
  .panel-counselling .copy { position: absolute; left: 226px; top: 14px; right: 22px; }
  .divider { position: absolute; left: 34px; top: 540px; width: 795px; height: 6px; background: var(--green); }
  .panel-hypno { top: 602px; height: 300px; padding: 14px 22px 14px 14px; }
  .panel-hypno .photo { float: right; width: 166px; height: 152px; margin: 4px 0 8px 24px;
    background: linear-gradient(135deg, #e6dccb, #b59a78 55%, #7c6449); }
  .contact { position: absolute; left: 34px; top: 935px; color: var(--purple); font-size: 19px; line-height: 1.3; font-style: normal; }
  .tagline {
    position: absolute; left: 34px; top: 1126px; width: 795px; text-align: center;
    border-top: 3px solid var(--green); padding-top: 14px;
    color: var(--purple); font-size: 24px;
  }
</style>
</head>
<body>
<div class="flyer">
  <header class="brand">
    <div class="brand-mark"></div>
    <div class="brand-name">Wrenlow<br>Counselling &amp;<br>Hypnotherapy</div>
  </header>
  <p class="quote">Sometimes when I'm in the boat alone, it doesn't feel like I have any oars. … up out of the fog, I can see your harbour light somewhere out there, guiding me in.</p>

  <nav class="nav">
    <span>Clarify</span><span>Growth and development</span><span>Explore</span><span>Behaviour change</span>
  </nav>

  <h2 class="section-title" style="top:332px">To Talk, To be Heard, To be You</h2>
  <section class="panel panel-counselling">
    <div class="photo" role="img" aria-label="Photo of a calm counselling room with armchairs"></div>
    <div class="copy">
      <h3>What is counselling?</h3>
      <p>It's about being able to have a safe and trusted environment where you feel comfortable to share whatever is going on for you, problems, concerns, areas you'd like to personally develop. Essentially, it's time for you to just be you, free from any form of judgement.</p>
    </div>
  </section>
  <div class="divider"></div>

  <h2 class="section-title" style="top:556px">Relax, Free Your Mind, Take Control</h2>
  <section class="panel panel-hypno">
    <div class="photo" role="img" aria-label="Photo of a relaxing therapy room with a reclining chair"></div>
    <h3>What is Hypnotherapy?</h3>
    <p>What comes to mind? You may conjure up images or thoughts of stage shows. In reality, real hypnosis bears little resemblance to that and can be far more beneficial. It's all about slowing down the pace of life in order to allow your mind to receive positive suggestions for change. You've probably already experienced something similar to hypnosis and not even known it. Have you ever been on a train journey, sat there with half-closed eyes, day-dreaming or driven a journey and suddenly wonder how you reached your destination? In that boundary between sleep and awake our brain produces alpha waves – that's where I can help guide your unconscious mind to solve the problems that your conscious brain can't do on its own.</p>
  </section>

  <address class="contact">
    CONTACT INFORMATION<br>
    Postal and location address:<br>
    Wrenlow Counselling and Hypnotherapy.<br>
    12 Mill Lane, Ashcombe, AC4 2LR<br>
    Phone : 07700 900412<br>
    Email: wrenlowtherapy@mailbox.co.uk
  </address>

  <p class="tagline">Trusted &nbsp;•&nbsp; An approach tailored to you &nbsp;•&nbsp; Professional</p>
</div>
</body>
</html>
```